Copper Lantern Stationery Design COMMITTED PAY

We need you to design stationary for a new Business called Copper Lantern. We have already got the logo designed and it is attached. Obviously we're looking for a stationery set designed around the colours and style to match the logo.

Use generic name, address, phone, fax, email etc ... I will edit text to required details.

What we need:
- Business Card Design Double Sided (90 x 55m + Bleed 3mm+)
- A4 Letter head Design
- A4 Presentation Folder Design
- Invoice Header Approx 210 x 55mm (Include Logo & Images)

And whatever other bonuses you'd like to kick in associated with the package.

I've attached some images and I've got hundreds more. If you want something else in the way of images, let me know.

I look forward to your seeing your designs.
Updates

Thought I should just clarify the follwoing:

1. The Invoice Header is just a branding for the top of my accounting package form.  It is not contain any contact information or the like.  Just logo, some images and some of your creativity and flair to bring it together.
2. The business does synthetic grass (75% of the business), Wetpour Rubber Surfaces, Softfall Surfaces and Rubber Wood Mulch.  These are categories you might choose to somehow highlight on the letterhead.
3. Business Card reverse side should be used to highlight the categories using images provided.

Wow, I've had some really nice designs submitted thus far, but my concern is that I can't just have an awesome looking card.  I really feel that my card needs to either show or say what we do.  Please make sure your design either shows or says the following:

- Synthetic Grass
- Wetpour Rubber Surfaces
- Softfall Surfaces
- Rubber Wood Mulch
- Shade Structures
- Landscape Structures

Just another note, don't know if I mentioned it or not in the original brief, but I prefer the use of icons instead of text for phone, email, fax etc labels.

Industry/Entity Type

Business

Requirements
Must have
• - Provide full editable source files
- Provide letterhead in MS Word format as well
- All designs must be awesome, but also show or say what we do. This is very important to me. I want anyone to look at our letterhead, business card etc and know instantly what it is that we do.
- Super quick turnaround on handover. I need card files to the printer on Monday morning (that's my Monday at GMT+10)
Nice to have
• - Creative use of the logo for a little bit of wow
Should not have
• - not square, boxy or rigid ... Loosen up a bit!

```html
<!DOCTYPE html>
<html lang="en">
<head>
<meta charset="utf-8">
<title>Copper Lantern — Business Card</title>
<link href="https://fonts.googleapis.com/css2?family=Roboto+Slab:wght@400;700&family=Open+Sans:wght@400;600&display=swap" rel="stylesheet">
<style>
  :root {
    --bg: #3a3a3a;
    --card: #f7f7f5;
    --ink: #3b3b3b;
    --blue: #1f9ad6;
    --green: #4aa832;
    --band: #1b1b1b;
    --grout: #8a8a8a;
  }
  * { margin: 0; padding: 0; box-sizing: border-box; }
  html, body { width: 1200px; height: 900px; overflow: hidden; }
  body { background: var(--bg); position: relative; font-family: "Roboto Slab", serif; }

  .card {
    position: absolute;
    width: 540px; height: 330px;
    border-radius: 3px;
    box-shadow: 0 10px 30px rgba(0,0,0,.45);
    overflow: hidden;
  }

  /* Back side: surface swatches */
  .card-back {
    left: 70px; top: 90px;
    background: var(--grout);
    padding: 10px;
    display: grid;
    grid-template-columns: repeat(5, 1fr);
    grid-template-rows: 1fr 1fr 34px 1fr;
    gap: 8px;
  }
  .swatch { border-radius: 2px; }
  .swatch.green-dark { background: linear-gradient(135deg,#5aa83a,#3f8a28); }
  .swatch.green-lime { background: linear-gradient(135deg,#8fd35a,#6dbb3c); }
  .swatch.stone-white { background: linear-gradient(135deg,#e6e4de,#c9c6bf); }
  .swatch.tan { background: linear-gradient(135deg,#c7a06a,#a8814d); }
  .swatch.red { background: linear-gradient(135deg,#d0533f,#b03d2c); }
  .swatch.blue { background: linear-gradient(135deg,#3f8fd8,#2a6fb6); }
  .swatch.charcoal { background: linear-gradient(135deg,#56565c,#3a3a40); }
  .swatch.yellow { background: linear-gradient(135deg,#e9c51c,#cfa60e); }
  .swatch.orange { background: linear-gradient(135deg,#f08226,#d7650f); }
  .swatch.lemon { background: linear-gradient(135deg,#f1de3a,#d9c21d); }
  .swatch.purple { background: linear-gradient(135deg,#8e5fb8,#6f4398); }
  .swatch.teal { background: linear-gradient(135deg,#7fcfc4,#5bb3a8); }
  .swatch.cream { background: linear-gradient(135deg,#e8dcc4,#cdbd9f); }
  .swatch.sand { background: linear-gradient(135deg,#d8b787,#bd9863); }
  .swatch.grey-light { background: linear-gradient(135deg,#b9b9b9,#9a9a9a); }

  .web-band {
    grid-column: 1 / -1;
    background: var(--band);
    color: #e8e8e8;
    font-family: "Open Sans", sans-serif;
    font-size: 14px;
    letter-spacing: .5px;
    display: flex; align-items: center; justify-content: center;
    margin: 0 -10px;
  }

  /* Front side */
  .card-front {
    left: 600px; top: 480px;
    background: var(--card);
    color: var(--ink);
  }
  .brand {
    position: absolute; left: 34px; top: 40px;
    display: flex; align-items: center; gap: 12px;
  }
  .brand-dot {
    width: 36px; height: 36px; border-radius: 50%;
    border: 3px solid var(--blue);
  }
  .brand-name {
    font-weight: 700; font-size: 26px; color: var(--green);
    line-height: 1; text-transform: uppercase;
  }
  .tagline {
    position: absolute; left: 82px; top: 76px;
    font-family: "Open Sans", sans-serif; font-weight: 600;
    font-size: 9.5px; color: var(--green);
  }
  .person { position: absolute; right: 56px; top: 28px; text-align: right; }
  .person-name { color: var(--blue); font-size: 18px; }
  .person-title { font-size: 12px; color: #444; }
  .decor-circle {
    position: absolute; right: 30px; top: 110px;
    width: 150px; height: 150px; border-radius: 50%;
    border: 6px solid var(--blue); opacity: .9;
  }
  .contact { position: absolute; left: 34px; bottom: 38px; list-style: none; font-size: 14px; line-height: 1.5; }
  .contact li { display: flex; align-items: flex-start; gap: 10px; }
  .contact svg { width: 14px; height: 14px; margin-top: 4px; flex: none; fill: var(--blue); }
</style>
</head>
<body>

<section class="card card-back" aria-label="Business card back">
  <div class="swatch green-dark" role="img" aria-label="Dark green rubber crumb sample"></div>
  <div class="swatch green-lime" role="img" aria-label="Lime green rubber crumb sample"></div>
  <div class="swatch stone-white" role="img" aria-label="White rubber crumb sample"></div>
  <div class="swatch tan" role="img" aria-label="Tan rubber crumb sample"></div>
  <div class="swatch red" role="img" aria-label="Red rubber crumb sample"></div>
  <div class="swatch blue" role="img" aria-label="Blue rubber crumb sample"></div>
  <div class="swatch charcoal" role="img" aria-label="Charcoal rubber crumb sample"></div>
  <div class="swatch yellow" role="img" aria-label="Yellow rubber crumb sample"></div>
  <div class="swatch orange" role="img" aria-label="Orange rubber crumb sample"></div>
  <div class="swatch lemon" role="img" aria-label="Lemon rubber crumb sample"></div>
  <div class="web-band">www.copperlantern.com</div>
  <div class="swatch purple" role="img" aria-label="Purple rubber crumb sample"></div>
  <div class="swatch teal" role="img" aria-label="Teal rubber crumb sample"></div>
  <div class="swatch cream" role="img" aria-label="Cream rubber crumb sample"></div>
  <div class="swatch sand" role="img" aria-label="Sand rubber crumb sample"></div>
  <div class="swatch grey-light" role="img" aria-label="Light grey rubber crumb sample"></div>
</section>

<section class="card card-front" aria-label="Business card front">
  <div class="brand">
    <span class="brand-dot"></span>
    <span class="brand-name">Copper Lantern</span>
  </div>
  <p class="tagline">Synthetic Grass &amp; Softfall Rubber Surfaces</p>

  <div class="person">
    <p class="person-name">Mara Ellison</p>
    <p class="person-title">President</p>
  </div>

  <div class="decor-circle"></div>

  <ul class="contact">
    <li>
      <svg viewBox="0 0 24 24"><path d="M12 2a7 7 0 0 0-7 7c0 5 7 13 7 13s7-8 7-13a7 7 0 0 0-7-7zm0 9.5A2.5 2.5 0 1 1 12 6.5a2.5 2.5 0 0 1 0 5z"/></svg>
      <span>48 Linden Ridge Road,<br>Suite 210 Brookfield, CT 06804</span>
    </li>
    <li>
      <svg viewBox="0 0 24 24"><path d="M6.6 10.8a15 15 0 0 0 6.6 6.6l2.2-2.2a1 1 0 0 1 1-.25 11.4 11.4 0 0 0 3.6.57 1 1 0 0 1 1 1V20a1 1 0 0 1-1 1A17 17 0 0 1 3 4a1 1 0 0 1 1-1h3.5a1 1 0 0 1 1 1c0 1.25.2 2.45.57 3.6a1 1 0 0 1-.25 1z"/></svg>
      <span>860-555-0142</span>
    </li>
    <li>
      <svg viewBox="0 0 24 24"><path d="M2 5h20v14H2zm2 2v.5l8 5 8-5V7zm0 3v7h16v-7l-8 5z"/></svg>
      <span>hello@copperlantern.com</span>
    </li>
  </ul>
</section>

</body>
</html>
```